Accident Law Firm Billboard Bold Easy to See Car Accidents

We need a billboard design that can catch attention in a very crowed Car Accident lawyer market. We wish to feature the phone number (652) 318-4470 as the focus of the Bill Board. We are trying to get the phone number recognized and remembered by drivers. The law firm name is not as crucial to remember.
Basically, It's CAR ACCIDENT? Then (652) 318-4470. We are not married to any specific color scheme but it has to POP and catch attention.
So the Crucial elements are as follows:
1. Phone number (652) 318-4470
2. Words CAR ACCIDENT?
3. Firm Logo in lower portion or where appropriate. Firm Logo to be provided
4. We may want to try a Day Glow orange color, with White and Black added. An example of the color scheme shall be provided.
5. Possible "Catch Phrase" to be used, "It's Time Call 9"
Target Market(s)
Orlando Florida Car Accident victims
Industry/Entity Type
Law Firm
Requirements
Must have
- Easy to see phone number (652) 318-4470
- Catch attention
Nice to have
- I would like to have the sign visible in bright sunlight and it not too hard to immediately know what phone number is for
Should not have
- too many words
- No bold enough
- confusing fonts
- Unclear fonts

```html
<!DOCTYPE html>
<html lang="en">
<head>
<meta charset="utf-8">
<title>Marlowe Law Firm – Car Accident Billboards</title>
<link rel="stylesheet" href="https://fonts.googleapis.com/css2?family=Bebas+Neue&family=Montserrat:wght@300;400;700;800;900&display=swap">
<style>
  :root{
    --orange:#f5823d;
    --orange-deep:#e9621c;
    --orange-band:#f07a33;
    --black:#1a1a1a;
    --white:#ffffff;
    --page:#e8e8e8;
    --photo-light:#d9d9d9;
    --photo-dark:#3a3a3a;
  }
  html,body{margin:0;padding:0;overflow:hidden;}
  body{width:782px;height:1200px;background:var(--page);position:relative;font-family:"Montserrat",sans-serif;}
  .billboard{position:absolute;left:64px;width:640px;height:320px;box-shadow:0 4px 10px rgba(0,0,0,.35);}
  .billboard svg{display:block;width:640px;height:320px;}
  .billboard--one{top:40px;}
  .billboard--two{top:426px;}
  .billboard--three{top:814px;}
  .sample-label{position:absolute;right:78px;margin:0;font-size:13px;font-weight:400;color:#222;letter-spacing:.3px;}
  .sample-label--one{top:386px;}
  .sample-label--two{top:772px;}
  .sample-label--three{top:1160px;}
  .display{font-family:"Bebas Neue",sans-serif;}
  .heavy{font-family:"Montserrat",sans-serif;font-weight:800;}
  .light{font-family:"Montserrat",sans-serif;font-weight:300;}
  .firm{font-family:"Montserrat",sans-serif;font-weight:700;}
</style>
</head>
<body>

<section class="billboard billboard--one" aria-label="Billboard option 1">
  <svg viewBox="0 0 640 320" xmlns="http://www.w3.org/2000/svg">
    <defs>
      <linearGradient id="photoTone1" x1="0" y1="0" x2="1" y2="1">
        <stop offset="0" stop-color="var(--photo-light)"/>
        <stop offset="1" stop-color="var(--photo-dark)"/>
      </linearGradient>
    </defs>
    <rect class="panel-orange" width="640" height="256" fill="var(--orange)"/>
    <polygon class="chevron-band" points="462,0 496,0 368,152 456,256 418,256 330,152" fill="var(--orange-deep)"/>
    <polygon class="photo-area" role="img" aria-label="Black and white photo of a car with a crushed rear end" points="496,0 640,0 640,256 456,256 368,152" fill="url(#photoTone1)"/>
    <text class="display headline-car" x="26" y="134" font-size="160" fill="var(--white)" textLength="228" lengthAdjust="spacingAndGlyphs">CAR</text>
    <path class="headline-pill" d="M0 136 H270 a14 14 0 0 1 14 14 V178 a14 14 0 0 1 -14 14 H0 Z" fill="var(--black)"/>
    <text class="display headline-accident" x="24" y="184" font-size="64" fill="var(--white)" textLength="250" lengthAdjust="spacingAndGlyphs">ACCIDENT?</text>
    <text x="20" y="244" font-size="40" textLength="344" lengthAdjust="spacingAndGlyphs"><tspan class="light" fill="var(--black)">IT'S TIME </tspan><tspan class="heavy" fill="var(--white)">CALL 9</tspan></text>
    <rect class="contact-bar" y="256" width="640" height="64" fill="var(--black)"/>
    <g class="phone-icon" transform="translate(40 288)">
      <circle r="16" fill="var(--orange)"/>
      <path d="M-3 -9 q-6 9 0 18 l4 -1 -2 -5 -2 1 q-2 -4 0 -8 l2 1 2 -5 z" fill="var(--black)"/>
    </g>
    <text class="heavy phone-number" x="70" y="303" font-size="42" fill="var(--white)" textLength="370" lengthAdjust="spacingAndGlyphs">(652) 318-4470</text>
    <line class="divider" x1="463" y1="274" x2="463" y2="308" stroke="var(--orange)" stroke-width="2"/>
    <text class="firm" x="487" y="290" font-size="22" fill="var(--white)" textLength="134" lengthAdjust="spacingAndGlyphs">MARLOWE</text>
    <text class="firm" x="487" y="303" font-size="10" fill="var(--white)" textLength="134" lengthAdjust="spacing">LAW FIRM P.C.</text>
  </svg>
</section>
<p class="sample-label sample-label--one">BILLBOARD SAMPLE 1</p>

<section class="billboard billboard--two" aria-label="Billboard option 2">
  <svg viewBox="0 0 640 320" xmlns="http://www.w3.org/2000/svg">
    <defs>
      <linearGradient id="photoTone2" x1="0" y1="0" x2="1" y2="1">
        <stop offset="0" stop-color="var(--photo-light)"/>
        <stop offset="1" stop-color="var(--photo-dark)"/>
      </linearGradient>
    </defs>
    <rect class="panel-white" width="640" height="320" fill="var(--white)"/>
    <polygon class="photo-area" role="img" aria-label="Black and white photo of a car with a crushed rear end" points="352,0 640,0 640,256 438,256" fill="url(#photoTone2)"/>
    <text class="heavy headline-car" x="24" y="132" font-size="146" fill="var(--orange)" textLength="306" lengthAdjust="spacingAndGlyphs">CAR</text>
    <text class="heavy headline-accident" x="32" y="190" font-size="56" fill="var(--black)" textLength="320" lengthAdjust="spacingAndGlyphs">ACCIDENT?</text>
    <polygon class="slogan-band" points="0,200 420,200 438,256 0,256" fill="var(--orange)"/>
    <text x="20" y="244" font-size="44" textLength="394" lengthAdjust="spacingAndGlyphs"><tspan class="light" fill="var(--white)">IT'S TIME </tspan><tspan class="heavy" fill="var(--white)">CALL 9</tspan></text>
    <polygon class="contact-bar" points="264,256 640,256 640,320 228,320" fill="var(--black)"/>
    <text class="firm" x="18" y="290" font-size="22" fill="var(--black)" textLength="158" lengthAdjust="spacingAndGlyphs">MARLOWE</text>
    <text class="firm" x="18" y="304" font-size="10" fill="var(--black)" textLength="158" lengthAdjust="spacing">LAW FIRM P.C.</text>
    <g class="phone-icon" transform="translate(280 288)">
      <circle r="16" fill="var(--orange)"/>
      <path d="M-3 -9 q-6 9 0 18 l4 -1 -2 -5 -2 1 q-2 -4 0 -8 l2 1 2 -5 z" fill="var(--black)"/>
    </g>
    <text class="heavy phone-number" x="312" y="303" font-size="40" fill="var(--white)" textLength="308" lengthAdjust="spacingAndGlyphs">(652) 318-4470</text>
  </svg>
</section>
<p class="sample-label sample-label--two">BILLBOARD SAMPLE 2</p>

<section class="billboard billboard--three" aria-label="Billboard option 3">
  <svg viewBox="0 0 640 320" xmlns="http://www.w3.org/2000/svg">
    <defs>
      <radialGradient id="orangeGlow" cx="0.5" cy="0.4" r="0.8">
        <stop offset="0" stop-color="#f48a48"/>
        <stop offset="1" stop-color="var(--orange-deep)"/>
      </radialGradient>
      <filter id="textShadow" x="-5%" y="-10%" width="110%" height="130%">
        <feDropShadow dx="2" dy="3" stdDeviation="2" flood-color="#000" flood-opacity=".35"/>
      </filter>
    </defs>
    <rect class="panel-orange" width="640" height="256" fill="url(#orangeGlow)"/>
    <rect class="crash-illustration" role="img" aria-label="Illustration of two cars colliding head-on" x="220" y="30" width="200" height="46" rx="23" fill="#3a2a20" opacity=".85"/>
    <text class="display headline" x="320" y="186" font-size="132" text-anchor="middle" fill="var(--white)" filter="url(#textShadow)" textLength="586" lengthAdjust="spacingAndGlyphs">CAR ACCIDENT?</text>
    <text x="320" y="240" font-size="42" text-anchor="middle" textLength="394" lengthAdjust="spacingAndGlyphs"><tspan class="light" fill="var(--black)">IT'S TIME </tspan><tspan class="heavy" fill="var(--white)">CALL 9</tspan></text>
    <rect class="logo-field" y="256" width="640" height="64" fill="var(--white)"/>
    <polygon class="contact-bar" points="322,256 640,256 640,320 286,320" fill="var(--black)"/>
    <text class="firm" x="18" y="290" font-size="22" fill="var(--black)" textLength="158" lengthAdjust="spacingAndGlyphs">MARLOWE</text>
    <text class="firm" x="18" y="304" font-size="10" fill="var(--black)" textLength="158" lengthAdjust="spacing">LAW FIRM P.C.</text>
    <g class="phone-icon" transform="translate(280 288)">
      <circle r="16" fill="var(--orange)"/>
      <path d="M-3 -9 q-6 9 0 18 l4 -1 -2 -5 -2 1 q-2 -4 0 -8 l2 1 2 -5 z" fill="var(--black)"/>
    </g>
    <text class="heavy phone-number" x="312" y="303" font-size="40" fill="var(--white)" textLength="308" lengthAdjust="spacingAndGlyphs">(652) 318-4470</text>
  </svg>
</section>
<p class="sample-label sample-label--three">BILLBOARD SAMPLE 3</p>

</body>
</html>
```